Commercial Construction Company

We need a business card design based on our current logo. We are a commercial general contractor based in Southern California that specializes in bank remodels. We would like to see designs that incorporate dark blue. The final design should portray an image of professionalism and quality.

If possible, I would like to add metallic foil to the design. Thank you

```html
<!DOCTYPE html>
<html lang="en">
<head>
<meta charset="utf-8">
<title>Harlow Builders – Business Card</title>
<link href="https://fonts.googleapis.com/css2?family=Source+Sans+3:wght@400;600;700&display=swap" rel="stylesheet">
<style>
  :root {
    --navy: #0d4a8a;
    --ink: #1c1c1c;
    --paper: #f4f4f4;
    --band-grey: #b5b5b5;
    --rule: #8c8c8c;
    --stage: #d9dadc;
    --white: #ffffff;
  }
  * { box-sizing: border-box; margin: 0; padding: 0; }
  html, body { width: 1200px; height: 1021px; overflow: hidden; }
  body {
    background: var(--stage);
    font-family: "Source Sans 3", Arial, sans-serif;
    position: relative;
  }
  .card {
    position: absolute;
    left: 250px;
    width: 700px;
    height: 400px;
    overflow: hidden;
    box-shadow: 0 6px 18px rgba(0,0,0,.18);
  }
  /* Back side */
  .card--back { top: 60px; background: var(--navy); }
  .brand {
    position: absolute;
    display: flex;
    align-items: center;
    gap: 14px;
  }
  .brand__dot { width: 30px; height: 30px; border-radius: 50%; flex: none; }
  .brand__name { font-weight: 600; font-size: 46px; line-height: 1; white-space: nowrap; }
  .card--back .brand { left: 0; right: 0; top: 150px; justify-content: center; }
  .card--back .brand__dot { background: var(--white); }
  .card--back .brand__name { color: var(--white); }
  .license {
    position: absolute;
    left: 0; right: 0; bottom: 34px;
    text-align: center;
    color: var(--white);
    font-size: 20px;
    letter-spacing: 2px;
  }
  /* Front side */
  .card--front { top: 561px; background: var(--paper); }
  .front-band { position: absolute; inset: 0; }
  .card--front .brand { left: 40px; top: 112px; }
  .card--front .brand__dot { background: var(--navy); }
  .card--front .brand__name { color: var(--ink); font-size: 36px; }
  .divider {
    position: absolute;
    left: 372px; top: 60px;
    width: 2px; height: 200px;
    background: var(--rule);
  }
  .contact { position: absolute; left: 404px; top: 62px; }
  .contact__name { color: var(--navy); font-weight: 700; font-size: 26px; line-height: 1.1; }
  .contact__title { color: var(--ink); font-size: 20px; margin-bottom: 14px; }
  .contact__list { list-style: none; }
  .contact__item {
    display: flex; align-items: center; gap: 10px;
    font-size: 19px; color: var(--ink); line-height: 1.3;
    white-space: nowrap;
  }
  .contact__item svg { width: 16px; height: 16px; fill: var(--navy); flex: none; }
  .contact__item--web { color: var(--navy); }
  .address {
    position: absolute;
    left: 40px; bottom: 22px;
    color: var(--white);
    font-size: 19px;
  }
</style>
</head>
<body>

<section class="card card--back">
  <div class="brand">
    <span class="brand__dot"></span>
    <span class="brand__name">Harlow Builders</span>
  </div>
  <p class="license">Contractor's License #820415</p>
</section>

<section class="card card--front">
  <svg class="front-band" viewBox="0 0 700 400" preserveAspectRatio="none" aria-hidden="true">
    <path d="M0,262 C200,322 450,342 700,318 L700,400 L0,400 Z" fill="#b5b5b5"/>
    <path d="M0,272 C200,332 450,352 700,328 L700,400 L0,400 Z" fill="#0d4a8a"/>
  </svg>

  <div class="brand">
    <span class="brand__dot"></span>
    <span class="brand__name">Harlow Builders</span>
  </div>

  <div class="divider"></div>

  <div class="contact">
    <p class="contact__name">Daniel Reyes</p>
    <p class="contact__title">Founder &amp; Owner</p>
    <ul class="contact__list">
      <li class="contact__item">
        <svg viewBox="0 0 16 16"><path d="M3 1l3 3-1.5 2a9 9 0 0 0 5.5 5.5L12 10l3 3-2 2C7 15 1 9 1 3z"/></svg>
        (909) 555-0148
      </li>
      <li class="contact__item">
        <svg viewBox="0 0 16 16"><path d="M3 1l3 3-1.5 2a9 9 0 0 0 5.5 5.5L12 10l3 3-2 2C7 15 1 9 1 3z"/></svg>
        (833) 555-0172 Toll Free
      </li>
      <li class="contact__item">
        <svg viewBox="0 0 16 16"><rect x="4" y="1" width="8" height="4"/><rect x="1" y="6" width="14" height="6" rx="1"/><rect x="4" y="11" width="8" height="4"/></svg>
        (909) 555-0193
      </li>
      <li class="contact__item">
        <svg viewBox="0 0 16 16"><path d="M1 3h14v10H1z M2 4l6 5 6-5" fill="none" stroke="#0d4a8a" stroke-width="1.6"/></svg>
        daniel@harlowbuilders.com
      </li>
      <li class="contact__item contact__item--web">
        <svg viewBox="0 0 16 16"><circle cx="8" cy="8" r="6.5" fill="none" stroke="#0d4a8a" stroke-width="1.5"/><path d="M1.5 8h13M8 1.5c-3 3.5-3 9.5 0 13M8 1.5c3 3.5 3 9.5 0 13" fill="none" stroke="#0d4a8a" stroke-width="1.2"/></svg>
        www.harlowbuilders.com
      </li>
    </ul>
  </div>

  <p class="address">4417 Meridian Park Way, Suite 310, Fontana, CA 92335</p>
</section>

</body>
</html>
```